Website Design for Chef Varo Chinese Restaurant

Chef Varo is a new Chinese Restaurant. It offers exceptional dining experience with authentic and dynamic dishes created with quality ingredients.

A vivid website theme is required to promote this new restaurant online. Logo, menu, wine list and a few other files are attached for help with designing.

A very rough demo website has been setup and can be accessed via http://www.chefvaro.com.au. It is for telling designers what content is shown up on each page (except for homepage). By reading the about us page, designers can get some more info of Chef Varo. However, the layout, theme color, font, etc are not set in stone. Visitors should be able to feel Chef Varo restaurant's authentic Chinese cuisine and high hygiene standard. Home page of the website could be The "Our website is coming soon" description is shown on demo site but do not required to be presented on new design.

Some main pages design should be included: Home (landing page), About us, Menu (Dishes), Winelist, Gallery, Contact us. No HTML and coding required. The output should be well layered psd or png files with acceptable resolution for web use.

A few other website can be referred to are:

http://belmiraeatery.com.au/
http://www.stone-kettle.com/
http://quillhaven.com.au/
http://meadowbistro.com.au/
http://www.lanternvaledining.com.au/
http://www.thetrove.com.au/

Industry/Entity Type

Restaurant

Requirements
Nice to have
• I expect designs of at least these webpages: homepage, menu page and contact us page. If you can provide "about us" page as well, it will probably help you win the competition. well layered psd or png file is my preference.
Should not have
• You don't have to make html/cs/js or any coding. All I need is just art design

```html
<!DOCTYPE html>
<html lang="en">
<head>
<meta charset="utf-8">
<title>Chef Varo Chinese Restaurant</title>
<link href="https://fonts.googleapis.com/css2?family=Open+Sans:wght@400;600&family=Dancing+Script:wght@700&family=Noto+Serif:wght@400;700&family=Roboto:wght@400&display=swap" rel="stylesheet">
<style>
:root{
  --cream:#f8f6c2;
  --red:#e8454a;
  --red-dark:#c9362f;
  --text-red:#c93b34;
  --body:#444;
  --dark:#474747;
  --line:#dcdcdc;
  --star:#f2a93b;
}
*{margin:0;padding:0;box-sizing:border-box}
html,body{width:1200px;height:2184px;overflow:hidden;background:#fff;font-family:"Open Sans",sans-serif;color:var(--body)}
.page{position:relative;width:1200px;height:2184px}
.abs{position:absolute}
.header{left:0;top:0;width:1200px;height:149px;background:var(--cream)}
.brand{left:0;top:17px;width:1200px;text-align:center}
.brand-mark{display:inline-block;width:34px;height:54px;background:var(--red-dark)}
.brand-name{margin-top:12px;font-family:"Noto Serif",serif;font-weight:700;font-size:21px;color:#1e1e1e;letter-spacing:.4px}
.nav{left:0;top:149px;width:1200px;height:52px;background:var(--cream);border-top:1px solid #e6e3b0;border-bottom:1px solid #e6e3b0}
.nav ul{position:absolute;left:140px;top:0;display:flex;list-style:none;height:52px}
.nav li{height:52px;line-height:52px;text-align:center;font-size:14px;color:#333;border-right:1px solid #e2dfad}
.nav li.active{background:#333;color:#fff}
.hero{left:0;top:201px;width:1200px;height:505px;background:var(--red)}
.slide{left:140px;top:29px;width:918px;height:424px;background:#fff;box-shadow:0 2px 6px rgba(0,0,0,.35);overflow:hidden}
.slide-photo{left:0;top:0;width:560px;height:424px;background:
  radial-gradient(ellipse 230px 150px at 230px 110px,#9c2f16 0%,#b8452a 45%,rgba(184,69,42,0) 100%),
  radial-gradient(ellipse 320px 260px at 250px 280px,#f3e2a8 0%,#efd896 55%,rgba(246,240,225,0) 100%),
  linear-gradient(90deg,#ece4cc 0%,#f6f2e8 75%,#fff 100%)}
.slogan{left:530px;top:100px;width:380px;font-family:"Dancing Script",cursive;font-weight:700;font-size:33px;line-height:49px;color:var(--text-red);white-space:nowrap}
.dots{left:687px;top:282px;display:flex;gap:4px}
.dots span{width:14px;height:14px;border-radius:50%;background:#444}
.dots span:first-child{background:var(--red)}
h2{font-family:"Roboto",sans-serif;font-weight:400;color:#333}
.about-title{left:0;top:745px;width:1200px;text-align:center;font-size:25px}
.about-text{left:130px;top:806px;width:940px;text-align:center;font-size:11.5px;line-height:21px;color:#444;white-space:nowrap}
.more{left:0;top:910px;width:1200px;text-align:center;font-size:13px;color:var(--text-red)}
.menu-title{left:0;top:967px;width:1200px;text-align:center;font-size:25px}
.dish{width:284px}
.dish-card{position:relative;width:284px;height:176px;border:1px solid var(--line)}
.dish-photo{position:absolute;left:30px;top:14px;width:224px;height:148px}
.ph-dumpling{background:radial-gradient(ellipse 90px 45px at 50% 60%,#e6dcb8 0%,#efe7cc 60%,rgba(255,255,255,0) 100%),radial-gradient(circle 22px at 82% 25%,#3c7a2a 0%,rgba(60,122,42,0) 100%)}
.ph-ribs{background:radial-gradient(circle 50px at 50% 50%,#a8502f 0%,#c67a45 55%,rgba(0,0,0,0) 70%),radial-gradient(circle 74px at 50% 52%,#e0a862 0%,#eabf7c 80%,rgba(255,255,255,0) 100%)}
.ph-cake{background:radial-gradient(ellipse 60px 50px at 48% 55%,#a8542c 0%,#c06a38 70%,rgba(0,0,0,0) 90%),radial-gradient(circle 85px at 50% 55%,#f4eeee 0%,#f7f3f3 85%,rgba(255,255,255,0) 100%)}
.price{position:absolute;left:0;top:0;width:64px;height:46px;background:var(--red-dark);color:#fff;font-family:"Noto Serif",serif;font-weight:700;font-size:14px;padding:10px 0 0 8px;clip-path:polygon(0 0,100% 0,100% 100%,50% 78%,0 100%)}
.dish-name{margin-top:14px;font-family:"Noto Serif",serif;font-weight:700;font-size:13.5px;color:var(--text-red)}
.stars{margin-top:6px;display:flex}
.arrows{display:flex}
.gallery-title{left:140px;top:1328px;font-size:25px}
.thumb{width:181px;height:130px;border:1px solid var(--line);padding:6px}
.thumb div{width:100%;height:100%}
.g1{background:radial-gradient(circle 30px at 50% 40%,#8b4a26 0%,rgba(139,74,38,0) 100%),radial-gradient(ellipse 70px 52px at 50% 55%,#dba863 0%,#e8c188 80%,rgba(255,255,255,0) 100%)}
.g2{background:radial-gradient(ellipse 60px 18px at 48% 48%,#d4802e 0%,#e39a48 70%,rgba(255,255,255,0) 100%),radial-gradient(ellipse 75px 45px at 50% 55%,#eee6d4 0%,rgba(255,255,255,0) 100%)}
.g3{background:radial-gradient(circle 30px at 50% 48%,#e2a98a 0%,#cfd7b0 60%,rgba(0,0,0,0) 100%),radial-gradient(ellipse 70px 50px at 50% 52%,#dfe8ee 0%,#eef3f6 80%,rgba(255,255,255,0) 100%)}
.g4{background:radial-gradient(ellipse 50px 55px at 48% 52%,#8c3a1a 0%,#b05a2a 60%,rgba(255,255,255,0) 100%)}
.g5{background:radial-gradient(ellipse 62px 40px at 50% 55%,#d98f4a 0%,#e7b06e 60%,rgba(255,255,255,0) 100%)}
.g6{background:radial-gradient(circle 32px at 50% 48%,#f0a830 0%,#f1b84a 55%,rgba(0,0,0,0) 75%),radial-gradient(ellipse 72px 52px at 50% 55%,#d9a25e 0%,#e6bd83 80%,rgba(255,255,255,0) 100%)}
.hours{left:772px;top:1337px;width:286px;border:1px solid var(--line)}
.hours-head{height:54px;line-height:54px;background:var(--red);color:#fff;text-align:center;font-size:16px}
.hours-row{display:flex;align-items:center;height:40px;border-top:1px solid var(--line);font-size:12px}
.hours-row .day{width:128px;padding-left:38px;color:var(--text-red)}
.hours-row .time{margin-left:14px;color:#333;font-size:13px}
.offer{left:0;top:1734px;width:1200px;height:150px;background:var(--red)}
.ribbon{left:140px;top:0;width:93px;height:130px;background:#3b3b3b;clip-path:polygon(0 0,100% 0,100% 100%,50% 88%,0 100%)}
.ribbon p{font-family:"Dancing Script",cursive;font-weight:700;color:#fff;font-size:20px;line-height:24px;text-align:center;padding-top:22px}
.ribbon hr{width:58px;margin:14px auto 0;border:0;border-top:1px solid #888}
.offer-title{left:301px;top:24px;font-size:25px;color:#fff}
.offer-text{left:301px;top:71px;width:780px;font-size:11.8px;line-height:21px;color:#fff}
.footer{left:0;top:1884px;width:1200px;height:213px;background:var(--dark);color:#fff}
.fc-title{left:140px;top:24px;font-family:"Noto Serif",serif;font-weight:400;font-size:24px;color:#ccc}
.fc-text{left:140px;top:76px;width:240px;font-size:12px;line-height:21.5px;white-space:nowrap}
.recent-title{left:493px;top:34px;font-family:"Noto Serif",serif;font-weight:400;font-size:14px}
.recipe{display:flex;gap:14px;width:250px}
.recipe-photo{width:84px;height:76px;flex:none}
.r1{background:radial-gradient(ellipse 40px 30px at 45% 55%,#c8472a 0%,#d9724a 55%,#efd2b4 100%)}
.r2{background:radial-gradient(circle 32px at 50% 52%,#d77020 0%,#e9a04a 55%,#f4e2c2 100%)}
.recipe h4{font-family:"Noto Serif",serif;font-weight:400;font-size:12px}
.recipe p{font-size:12px;line-height:17px;margin-top:4px}
.recipe time{display:block;font-family:"Noto Serif",serif;font-size:12px;margin-top:6px}
.bottom{left:0;top:2097px;width:1200px;height:87px;background:var(--red);color:#fff}
.bottom-links{left:140px;top:23px;font-size:12px}
.copy{left:140px;top:50px;font-size:12px}
.social{left:910px;top:28px;display:flex;gap:15px}
.social span{width:25px;height:25px;border-radius:50%;background:#b8354e}
</style>
</head>
<body>
<div class="page">
  <header class="header abs">
    <div class="brand abs"><span class="brand-mark"></span><div class="brand-name">Chef Varo Chinese Restaurant</div></div>
  </header>
  <nav class="nav abs"><ul>
    <li class="active" style="width:93px">Home</li><li style="width:141px">About Us</li><li style="width:121px">Menu</li><li style="width:122px">Wine List</li><li style="width:122px">Gallery</li><li style="width:146px">Contact Us</li><li style="width:173px">Belmira Court</li>
  </ul></nav>

  <section class="hero abs">
    <div class="slide abs">
      <div class="slide-photo abs" role="img" aria-label="Plate of gnocchi topped with minced meat sauce and basil"></div>
      <p class="slogan abs">We offer an exceptional<br>dining experience with<br>authentic and dynamic dishes</p>
      <div class="dots abs"><span></span><span></span><span></span></div>
    </div>
  </section>

  <h2 class="about-title abs">About Us</h2>
  <p class="about-text abs">We offer exceptional dining experience with authentic and dynamic dishes created with quality ingredients. The menu of Chef Varo is based on classic Cantonese<br>Dishes, featured by southern China's local flavour characteristics. Taking advantages of South Australia's rich and quality food resources, Chef Varo developed a<br>Number of recipes to turn best ingredients into authentic dishes. All dishes are well looked after by Mr Varo's personally cares. We also offer Yam Cha, southern<br>Chinese style morning or afternoon tea, at lunch time. they are all same day hand made for garenteed freshness</p>
  <div class="more abs">MORE &nbsp;<svg width="9" height="13" viewBox="0 0 9 13"><path d="M2 1l5 5.5L2 12" fill="none" stroke="#c93b34" stroke-width="2"/></svg></div>

  <h2 class="menu-title abs">Menu,s</h2>
  <svg width="0" height="0" style="position:absolute"><defs><path id="st" d="M7 0l2 4.6 5 .4-3.8 3.2 1.2 4.8L7 10.4 2.6 13l1.2-4.8L0 5l5-.4z" fill="#f2a93b"/></defs></svg>
  <div class="dish abs" style="left:140px;top:1024px"><div class="dish-card"><div class="dish-photo ph-dumpling" role="img" aria-label="Vegetarian dumplings on a white plate"></div><div class="price">$50.00</div></div><div class="dish-name">Vegetarian Dumplings</div><div class="stars"><svg width="84" height="14"><use href="#st"/><use href="#st" x="17"/><use href="#st" x="34"/><use href="#st" x="51"/><use href="#st" x="68"/></svg></div></div>
  <div class="dish abs" style="left:457px;top:1024px"><div class="dish-card"><div class="dish-photo ph-ribs" role="img" aria-label="Steamed pork ribs in a bamboo basket"></div><div class="price">$40.00</div></div><div class="dish-name">Steamed Pork Ribs</div><div class="stars"><svg width="84" height="14"><use href="#st"/><use href="#st" x="17"/><use href="#st" x="34"/><use href="#st" x="51"/><use href="#st" x="68"/></svg></div></div>
  <div class="dish abs" style="left:763px;top:1024px"><div class="dish-card"><div class="dish-photo ph-cake" role="img" aria-label="Slice of Malay sponge cake with a flower"></div><div class="price">$560.00</div></div><div class="dish-name">Malay Cakes</div><div class="stars"><svg width="84" height="14"><use href="#st"/><use href="#st" x="17"/><use href="#st" x="34"/><use href="#st" x="51"/><use href="#st" x="68"/></svg></div></div>
  <div class="arrows abs" style="left:1028px;top:1241px"><svg width="26" height="14" viewBox="0 0 26 14"><path d="M8 2L3 7l5 5M18 2l5 5-5 5" fill="none" stroke="#111" stroke-width="2.6"/></svg></div>

  <h2 class="gallery-title abs">Gallery</h2>
  <div class="arrows abs" style="left:689px;top:1338px"><svg width="26" height="14" viewBox="0 0 26 14"><path d="M8 2L3 7l5 5M18 2l5 5-5 5" fill="none" stroke="#111" stroke-width="2.6"/></svg></div>
  <div class="thumb abs" style="left:140px;top:1399px"><div class="g1" role="img" aria-label="Braised meatball in a bamboo steamer"></div></div>
  <div class="thumb abs" style="left:342px;top:1399px"><div class="g2" role="img" aria-label="Fried dough rolls on a leaf"></div></div>
  <div class="thumb abs" style="left:540px;top:1399px"><div class="g3" role="img" aria-label="Bowl of noodle soup with greens"></div></div>
  <div class="thumb abs" style="left:140px;top:1552px"><div class="g4" role="img" aria-label="Stir-fried noodles"></div></div>
  <div class="thumb abs" style="left:342px;top:1552px"><div class="g5" role="img" aria-label="Pan-fried radish cake squares"></div></div>
  <div class="thumb abs" style="left:540px;top:1552px"><div class="g6" role="img" aria-label="Egg tarts in a bamboo steamer"></div></div>

  <svg width="0" height="0" style="position:absolute"><defs><g id="clock"><circle cx="6" cy="6" r="4.5" fill="none" stroke="#333" stroke-width="1.5"/><path d="M6 3.5V6h2" fill="none" stroke="#333" stroke-width="1.3"/></g></defs></svg>
  <aside class="hours abs">
    <div class="hours-head">Opening Hours</div>
    <div class="hours-row"><span class="day">Monday</span><svg width="12" height="12"><use href="#clock"/></svg><span class="time">10:00 - 20:00</span></div>
    <div class="hours-row"><span class="day">Tuesday</span><svg width="12" height="12"><use href="#clock"/></svg><span class="time">10:00 - 20:00</span></div>
    <div class="hours-row"><span class="day">Wednesday</span><svg width="12" height="12"><use href="#clock"/></svg><span class="time">10:00 - 20:00</span></div>
    <div class="hours-row"><span class="day">Tursday</span><svg width="12" height="12"><use href="#clock"/></svg><span class="time">10:00 - 20:00</span></div>
    <div class="hours-row"><span class="day">Friday</span><svg width="12" height="12"><use href="#clock"/></svg><span class="time">10:00 - 20:00</span></div>
    <div class="hours-row"><span class="day">Saturday</span><svg width="12" height="12"><use href="#clock"/></svg><span class="time">10:00 - 20:00</span></div>
    <div class="hours-row"><span class="day">Sunday</span><svg width="12" height="12"><use href="#clock"/></svg><span class="time">10:00 - 20:00</span></div>
  </aside>

  <section class="offer abs">
    <div class="ribbon abs"><p>Special<br>Offer!</p><hr></div>
    <h2 class="offer-title abs" style="color:#fff">Special Offer Of The Month $25%</h2>
    <p class="offer-text abs">Long established fact that a reader will be distracted by the readable content of a page when looking at its layout. The point of using<br>Lorem Ipsum is that it has a more-or-less normal distribution of letters, as opposed to using 'Content here</p>
  </section>

  <footer class="footer abs">
    <h3 class="fc-title abs">Food &amp; Cook</h3>
    <p class="fc-text abs">Lorem ipsum dolor sit amet, consectetur<br>Ut enim ad minim veniam, quis nostrud<br>exercitation &nbsp;ullamco &nbsp;laboris &nbsp;nisi &nbsp;ut<br>aliquip ex ea commodo</p>
    <h3 class="recent-title abs">RECENT RECIPES</h3>
    <div class="recipe abs" style="left:493px;top:80px"><div class="recipe-photo r1" role="img" aria-label="Frozen crab dish"></div><div><h4>Frozen Crab</h4><p>Lorem ipsum dolor sit amet, consectetur</p><time>June 7, 2013</time></div></div>
    <div class="recipe abs" style="left:829px;top:80px"><div class="recipe-photo r2" role="img" aria-label="Frozen crab in a bowl"></div><div><h4>Frozen Crab</h4><p>Lorem ipsum dolor sit amet, consectetur</p><time>June 7, 2013</time></div></div>
  </footer>

  <div class="bottom abs">
    <div class="bottom-links abs">Home | About Us | Menu | Wine List | Gallery | Contact Us | Belmira Court</div>
    <div class="copy abs">© Copyright.varochineserest. 2014</div>
    <div class="social abs"><span></span><span></span><span></span><span></span></div>
  </div>
</div>
</body>
</html>
```